El Molinero Brochure

Create a brochure for a new reception venue - El Molinero
www.El-Molinero.example

Here is info it must contain

Please refer to our site for inspiration - I know this is alot of info but ?

El Molinero Reception Hall
4817C Tidewell Rd, Benicia, CA 707-555-0148
www.El-Molinero.example

Located in Harborview, California, we are a new venue that can host a variety of events. We can provide an exceptional space for your next party, reception, quinceañera, birthday party, or meeting! We treat each client with respect and go out of our way to accommodate all of your needs and make your event a success. Conveniently located just off the 9/14 junction, El Molinero is located in a safe, well-lit area with a large private parking area.

The space comes prepared with everything you need to get your party started – chairs and tables with tablecloths, a well-equipped kitchen, and incredible decorations to set the perfect backdrop to your event! Rent just the Lounge for a more intimate get-together, or add the Main Hall for your large sit-down event.

Lounge – Beautiful 1,600 ft2 entry room featuring large living room with conversation sofa seating for 40+ Sound system  Pass-through bar with seating  Fully-equipped 200 ft2 kitchen with
4-burner gas stove, oven, large double sink, full-size refrigerator, 2 microwaves, and ice machine, plus lots of storage and counter space  Newly-remodeled Men’s and Women’s bathrooms

Main Hall – Spacious 24’x80’ room with seating for up to 160 people  2,000 ft2  72” round tables with chairs, each seating up to 8 guests  DJ stand and Sound system  Atmospheric lighting
_______________________________________
Pricing -
Daytime Parties
Available 8AM-2PM
4-hour minimum

Lounge and Kitchen Only
Fri - Sat - Sun : $80/hr
Mon - Thurs : $60/hr

All Areas: Lounge, Kitchen, Main Hall, and Backyard
Fri - Sat - Sun : $120/hr
Mon - Thurs : $100/hr
___________________________________________
Evening Events
Available 3PM-12AM
5-hour minimum

Lounge and Kitchen Only -
Fri - Sat - Sun : $100/hr
Mon - Thurs : $50/hr

Fri - Sat - Sun : $160/hr
Mon - Thurs : $75/hr
___________________________________________________
Looking for a different time frame, all-day rental, or other special request? Let us know!
We'd be happy to provide you with a custom quote for your event.

```html
<!DOCTYPE html>
<html lang="en">
<head>
<meta charset="utf-8">
<title>El Molinero Brochure</title>
<link href="https://fonts.googleapis.com/css2?family=Dancing+Script:wght@500&family=Source+Sans+3:wght@400;600;700&display=swap" rel="stylesheet">
<style>
:root{
  --backdrop:#1c1c1c;
  --cream:#fdf8ea;
  --cream-deep:#f6ecd0;
  --gold:#f7dc8f;
  --wine:#5c211b;
  --wine-dark:#3f1512;
  --ring:#a8736c;
  --ink:#5a2b22;
  --accent:#c0282e;
  --photo-a:#a88a6a;
  --photo-b:#3e2d22;
}
*{margin:0;padding:0;box-sizing:border-box}
html,body{width:1200px;height:1000px;overflow:hidden;background:var(--backdrop)}
body{position:relative;font-family:"Source Sans 3",Arial,sans-serif;color:var(--ink)}
.spread{position:absolute;display:flex;box-shadow:0 4px 14px rgba(0,0,0,.6)}
.spread-outside{left:65px;top:30px;width:575px;height:445px}
.spread-inside{left:509px;top:507px;width:575px;height:444px}
.panel{position:relative;height:100%;overflow:hidden}
.script{font-family:"Dancing Script",cursive;font-weight:500;color:var(--ink)}
.photo{background:radial-gradient(circle at 50% 35%,#f3d9a4 0,var(--photo-a) 30%,var(--photo-b) 85%)}

/* Pricing panel */
.pricing{width:188px;background:linear-gradient(var(--cream),var(--cream-deep));padding:14px 14px 0}
.pricing h2{font-size:19px;line-height:24px;margin-bottom:10px}
.price-group{font-size:7px;line-height:9px;margin-bottom:9px}
.price-group b{font-weight:700}
.rate{display:flex;justify-content:space-between}
.rate span.dots{flex:1;border-bottom:1px dashed #8a6a5a;margin:0 3px 3px}
.price-gap{height:14px}
.pricing-photo{position:absolute;left:0;bottom:0;width:188px;height:135px;
  -webkit-mask-image:linear-gradient(transparent,#000 30%);mask-image:linear-gradient(transparent,#000 30%)}

/* Quote panel */
.quote{width:197px;background:linear-gradient(100deg,var(--wine-dark),var(--wine) 40%,var(--wine-dark));color:var(--cream);text-align:center}
.quote-lead{position:absolute;top:52px;left:0;right:0;font-size:7.5px;line-height:10px}
.quote .script{position:absolute;top:74px;left:0;right:0;color:var(--cream);font-size:16px;line-height:20px}
.quote-sub{position:absolute;top:102px;left:0;right:0;font-size:7.5px;line-height:10px}
.ring-photo{position:absolute;border-radius:50%;border:7px solid var(--ring)}
.quote .ring-photo{left:29px;top:155px;width:144px;height:144px}
.contact{position:absolute;top:382px;left:0;right:0;font-size:7.5px;line-height:10.5px}
.contact b{font-weight:700}

/* Cover panel */
.cover{width:190px;background:linear-gradient(var(--cream),var(--gold))}
.brand{position:absolute;top:60px;left:35px;font-size:22px;font-weight:600;color:var(--ink);letter-spacing:.3px}
.tagline{position:absolute;top:86px;left:36px;font-size:8.5px;color:var(--accent)}
.ornament{position:absolute;top:112px;left:48px;width:92px;height:28px;background:linear-gradient(90deg,transparent,#c8a27a,transparent);opacity:.7;border-radius:50%}
.cover svg{position:absolute;left:0;top:195px}

/* About panel */
.about{width:188px;background:var(--cream);padding:14px 14px 0}
.about h2{font-size:18px;line-height:22px;margin-bottom:10px}
.about p{font-size:6.8px;line-height:10.5px;text-align:justify;margin-bottom:10px}
.about .ring-photo{left:17px;top:279px;width:150px;height:150px}

/* Gallery panel */
.gallery{width:198px}
.gallery svg{position:absolute;inset:0}

/* Areas panel */
.areas{width:189px;background:var(--cream);padding:12px 16px 0;text-align:center}
.areas h2{font-size:18px;line-height:20px}
.rule{border-top:1px dashed #8a6a5a;margin:7px 0 10px}
.areas h3{font-size:9px;font-weight:700;margin-bottom:2px}
.areas p{font-size:6.8px;line-height:10.5px;margin-bottom:12px}
.areas-photo{position:absolute;left:19px;top:296px;width:151px;height:90px;border:3px solid var(--ring)}
</style>
</head>
<body>

<section class="spread spread-outside">
  <div class="panel pricing">
    <h2 class="script">Pricing</h2>
    <div class="price-group"><b>Daytime Parties</b><br>Available 8AM-2PM<br>4-hour minimum</div>
    <div class="price-group"><b>Lounge and Kitchen Only</b>
      <div class="rate">Fri - Sat - Sun<span class="dots"></span>$80/hr</div>
      <div class="rate">Mon - Thurs<span class="dots"></span>$60/hr</div></div>
    <div class="price-group"><b>All Areas:<br>Lounge, Kitchen, Main Hall, Backyard</b>
      <div class="rate">Fri - Sat - Sun<span class="dots"></span>$120/hr</div>
      <div class="rate">Mon - Thurs<span class="dots"></span>$100/hr</div></div>
    <div class="price-gap"></div>
    <div class="price-group"><b>Evening Events</b><br>Available 3PM-12AM<br>5-hour minimum</div>
    <div class="price-group"><b>Lounge and Kitchen Only</b>
      <div class="rate">Fri - Sat - Sun<span class="dots"></span>$100/hr</div>
      <div class="rate">Mon - Thurs<span class="dots"></span>$50/hr</div></div>
    <div class="price-group"><b>All Areas:<br>Lounge, Kitchen, Main Hall, Backyard</b>
      <div class="rate">Fri - Sat - Sun<span class="dots"></span>$160/hr</div>
      <div class="rate">Mon - Thurs<span class="dots"></span>$75/hr</div></div>
    <div class="pricing-photo photo" role="img" aria-label="Photo of the lounge with sofas and armchairs"></div>
  </div>

  <div class="panel quote">
    <p class="quote-lead">Looking for a different time frame,<br>all-day rental, or other special request?</p>
    <p class="script">Let us know!</p>
    <p class="quote-sub">We'd be happy to provide you with<br>a custom quote for your event.</p>
    <div class="ring-photo photo" role="img" aria-label="Photo of the main hall set with round tables under string lights"></div>
    <p class="contact"><b>El Molinero Reception Hall</b><br>4817C Tidewell Rd, Harborview, CA 95999<br>Phone: 707-555-0148<br>www.El-Molinero.example</p>
  </div>

  <div class="panel cover">
    <div class="brand">El Molinero</div>
    <div class="tagline">celebrations . events . moments</div>
    <div class="ornament" role="img" aria-label="Decorative flourish"></div>
    <svg width="190" height="250" viewBox="0 0 190 250">
      <defs>
        <radialGradient id="coverPhoto" cx="0.55" cy="0.3" r="0.8">
          <stop offset="0" stop-color="#e9d3a8"/><stop offset="0.4" stop-color="#8d7257"/><stop offset="1" stop-color="#3b2b20"/>
        </radialGradient>
      </defs>
      <path d="M0 20 Q120 15 150 140 Q160 210 130 250 L0 250 Z" fill="url(#coverPhoto)" role="img" aria-label="Photo of the lounge with pendant lights and windows"/>
      <path d="M0 12 Q130 5 160 140 Q168 210 140 250" fill="none" stroke="var(--wine)" stroke-width="6"/>
      <path d="M40 6 Q150 20 168 150 Q172 210 155 250" fill="none" stroke="var(--wine)" stroke-width="3"/>
    </svg>
  </div>
</section>

<section class="spread spread-inside">
  <div class="panel about">
    <h2 class="script">About the Venue</h2>
    <p>Located in Harborview, California, we are a new venue that can host a variety of events. We can provide an exceptional space for your next party, reception, quinceañera, birthday party, or meeting! We treat each client with respect and go out of our way to accommodate all of your needs and make your event a success.</p>
    <p>Conveniently located just off the 9/14 junction, El Molinero is located in a safe, well-lit area with a large private parking area.</p>
    <p>The space comes prepared with everything you need to get your party started – chairs and tables with tablecloths, a well-equipped kitchen, and incredible decorations to set the perfect backdrop to your event! Rent just the Lounge for a more intimate get-together, or add the Main Hall for your large sit-down event.</p>
    <div class="ring-photo photo" role="img" aria-label="Photo of the lounge seating area"></div>
  </div>

  <div class="panel gallery">
    <svg width="198" height="444" viewBox="0 0 198 444">
      <defs>
        <linearGradient id="galleryPhoto" x1="0" y1="0" x2="0" y2="1">
          <stop offset="0" stop-color="#6b5441"/><stop offset="0.2" stop-color="#c9a97c"/><stop offset="0.5" stop-color="#5a4332"/><stop offset="0.8" stop-color="#8a6c52"/><stop offset="1" stop-color="#3a2a20"/>
        </linearGradient>
      </defs>
      <rect width="198" height="444" fill="url(#galleryPhoto)" role="img" aria-label="Photos of the buffet table, lounge corner with lilies, and seating area"/>
      <path d="M0 135 Q150 130 178 0" fill="none" stroke="#fff" stroke-width="5"/>
      <path d="M0 128 Q140 120 165 0" fill="none" stroke="#fff" stroke-width="2"/>
      <path d="M18 444 Q30 310 198 288" fill="none" stroke="#fff" stroke-width="6"/>
      <path d="M40 444 Q60 340 198 310" fill="none" stroke="#fff" stroke-width="2"/>
    </svg>
  </div>

  <div class="panel areas">
    <h2 class="script">Areas to Fit<br>Any Size Party!</h2>
    <div class="rule"></div>
    <h3>Entry Lounge</h3>
    <p>Beautiful 1,600 sq ft entry room featuring large living room with conversation sofa seating for 40 Sound system – Pass-through bar with seating Newly-remodeled Men's and Women's bathrooms</p>
    <h3>Kitchen</h3>
    <p>Fully-equipped 200 sq ft kitchen – 4-burner gas stove and oven – Large double sink – Full-size refrigerator – 2 microwaves – Ice machine – Lots of storage and counter space</p>
    <h3>Main Hall</h3>
    <p>Spacious 24'x80' room with seating for up to 160 people – 2,000 sq ft – 72" round tables with chairs, each seating up to 8 guests – DJ stand and Sound system – Atmospheric lighting</p>
    <div class="areas-photo photo" role="img" aria-label="Photo of the buffet spread in the main hall"></div>
  </div>
</section>

</body>
</html>
```